A start up Private Wine Label for export to Asia.

We are looking for the best graphic design for our very first wine label Corvessa Vineyards and would like the following requirements:

1. Black background - explore and play around the shade of black
2. Gold Shimmery Colour Font
3. Font should be a cursive classic posh that says Corvessa Vineyards
4. We would like the front graphic design to be simple and elegant and has a traditional classic feel to it.

Target Market(s)

Small scale to test the upper class market for export to Asia

Font styles to use
Script

Colors

Designer to choose colors to be used in the design.

Requirements
Must have
• Gold font for the label Corvessa Vineyards with shimmery touch to it.
• Elegant black background.
• Simple but elegant design.
• Attractive to the upper class market in Asia.
Nice to have
• Explore and play around with your imagination.

```html
<!DOCTYPE html>
<html lang="en">
<head>
<meta charset="UTF-8">
<title>Corvessa Vineyards – Wine Label</title>
<link rel="stylesheet" href="https://fonts.googleapis.com/css2?family=Great+Vibes&display=swap">
<style>
  :root {
    --page-white: #ffffff;
    --label-black: #000000;
    --label-glow: #1a1a1a;
    --gold-light: #f6e27a;
    --gold-mid: #d6a445;
    --gold-deep: #9a6a22;
    --gold-warm: #e8b86a;
  }
  html, body {
    margin: 0;
    padding: 0;
    width: 1200px;
    height: 1200px;
    overflow: hidden;
    background: var(--page-white);
  }
  .canvas {
    position: relative;
    width: 1200px;
    height: 1200px;
    background: var(--page-white);
  }
  .wine-label {
    position: absolute;
    left: 231px;
    top: 240px;
    width: 728px;
    height: 718px;
    background: radial-gradient(ellipse at 50% 52%, var(--label-glow) 0%, #0b0b0b 45%, var(--label-black) 85%);
    overflow: hidden;
  }
  .ornament {
    position: absolute;
    left: 105px;
    width: 528px;
    height: 160px;
    background: linear-gradient(90deg, var(--gold-deep) 0%, var(--gold-warm) 30%, var(--gold-mid) 55%, var(--gold-warm) 75%, var(--gold-deep) 100%);
    opacity: 0.85;
  }
  .ornament--top {
    top: 0;
    clip-path: polygon(0 0, 100% 0, 100% 32%, 81% 38%, 78% 66%, 62% 69%, 50% 100%, 38% 69%, 22% 66%, 19% 38%, 0 32%);
  }
  .ornament--bottom {
    bottom: 0;
    clip-path: polygon(0 100%, 100% 100%, 100% 68%, 81% 62%, 78% 34%, 62% 31%, 50% 0, 38% 31%, 22% 34%, 19% 62%, 0 68%);
  }
  .brand {
    position: absolute;
    left: 0;
    right: 0;
    top: 250px;
    text-align: center;
    font-family: "Great Vibes", cursive;
    font-weight: 400;
  }
  .brand__name,
  .brand__sub {
    display: block;
    background: linear-gradient(100deg, var(--gold-deep) 0%, var(--gold-light) 30%, var(--gold-mid) 55%, var(--gold-light) 75%, var(--gold-deep) 100%);
    -webkit-background-clip: text;
    background-clip: text;
    color: transparent;
    line-height: 1;
  }
  .brand__name {
    font-size: 112px;
    letter-spacing: 1px;
  }
  .brand__sub {
    margin-top: 18px;
    font-size: 62px;
  }
</style>
</head>
<body>
  <div class="canvas">
    <section class="wine-label">
      <div class="ornament ornament--top" role="img" aria-label="Gold mandala lace ornament along the top edge"></div>
      <h1 class="brand" style="margin:0;">
        <span class="brand__name">Corvessa</span>
        <span class="brand__sub">Vineyards</span>
      </h1>
      <div class="ornament ornament--bottom" role="img" aria-label="Gold mandala lace ornament along the bottom edge"></div>
    </section>
  </div>
</body>
</html>
```